Business card design Brightvane

We need a business card for BRIGHTvane aimport and distribution company which sells personnel weight lifting accessories, mainly the dorvel brand of product using our current logo. This design should represent class and a ruggard feel.

Target Market(s)

Weight lifters, crossfitters and other lifting sports

Industry/Entity Type

Weight

Contact Information for Business Card

BRIGHTvane, Owen Palfrey, Cell: 027 918 603, Email: brightvane@mailnest.co.nz, www.brightvane.co.nz

Requirements
Nice to have
• a good looking business card

```html
<!DOCTYPE html>
<html lang="en">
<head>
<meta charset="utf-8">
<title>Brightvane Business Card</title>
<link rel="stylesheet" href="https://fonts.googleapis.com/css2?family=Oswald:wght@500&family=Kalam:wght@400&family=Open+Sans:wght@700&family=Lato:wght@400&display=swap">
<style>
  :root {
    --concrete-light: #a6a5a2;
    --concrete-dark: #8f8e8b;
    --band: #4a4846;
    --brand-blue: #2b6399;
    --rule-blue: #2a5f96;
    --ink: #1c1c1c;
    --ink-contact: #222222;
    --paper: #ffffff;
    --black: #0b0b0b;
  }
  html, body {
    margin: 0;
    padding: 0;
    width: 1200px;
    height: 712px;
    overflow: hidden;
    background: #ffffff;
  }
  .card {
    position: relative;
    width: 1200px;
    height: 712px;
    overflow: hidden;
    background: radial-gradient(ellipse at 60% 40%, var(--concrete-light) 0%, var(--concrete-dark) 100%);
  }
  .card-rules {
    position: absolute;
    inset: 0;
  }
  .monogram-area {
    position: absolute;
    left: 0;
    top: 143px;
    width: 470px;
    height: 569px;
  }
  .header-band {
    position: absolute;
    left: 0;
    top: 49px;
    width: 1040px;
    height: 73px;
    background: var(--band);
    display: flex;
    justify-content: space-between;
    align-items: center;
    padding: 0 40px 0 106px;
    box-sizing: border-box;
  }
  .header-letter {
    font-family: "Oswald", sans-serif;
    font-weight: 500;
    font-size: 64px;
    line-height: 1;
    color: var(--brand-blue);
  }
  .person-name {
    position: absolute;
    left: 492px;
    top: 248px;
    margin: 0;
    font-family: "Kalam", cursive;
    font-weight: 400;
    font-size: 66px;
    line-height: 1;
    color: var(--ink);
  }
  .contact-list {
    position: absolute;
    left: 484px;
    top: 416px;
    margin: 0;
    padding: 0;
    list-style: none;
    font-family: "Open Sans", sans-serif;
    font-weight: 700;
    font-size: 25px;
    line-height: 39px;
    color: var(--ink-contact);
  }
  .partner-badge {
    position: absolute;
    left: 388px;
    top: 597px;
    width: 212px;
    height: 95px;
    background: var(--paper);
    display: flex;
    align-items: center;
    justify-content: center;
    font-family: "Open Sans", sans-serif;
    font-weight: 700;
    font-size: 46px;
    color: var(--black);
  }
  .brand-lockup {
    position: absolute;
    left: 632px;
    top: 602px;
    display: flex;
    align-items: center;
    gap: 14px;
    font-family: "Lato", sans-serif;
    font-weight: 400;
    font-size: 56px;
    color: var(--brand-blue);
  }
  .brand-lockup-square {
    width: 60px;
    height: 60px;
    background: var(--brand-blue);
  }
  .corner-tile {
    position: absolute;
    left: 1043px;
    top: 590px;
    width: 157px;
    height: 122px;
    background: var(--black);
    display: flex;
    align-items: center;
    justify-content: center;
    font-family: "Open Sans", sans-serif;
    font-weight: 700;
    font-size: 24px;
    color: var(--paper);
  }
</style>
</head>
<body>
<div class="card">
  <svg class="monogram-area" role="img" aria-label="Large brand monogram decoration" viewBox="0 0 470 569" width="470" height="569">
    <defs>
      <linearGradient id="monogram-fill" x1="0" y1="0" x2="1" y2="1">
        <stop offset="0" stop-color="#2b6399" stop-opacity="0.75"/>
        <stop offset="1" stop-color="#4a4846" stop-opacity="0.55"/>
      </linearGradient>
    </defs>
    <rect x="0" y="0" width="470" height="569" fill="url(#monogram-fill)"/>
  </svg>

  <svg class="card-rules" viewBox="0 0 1200 712" width="1200" height="712" aria-hidden="true">
    <line x1="0" y1="24" x2="1200" y2="24" stroke="var(--rule-blue)" stroke-width="7"/>
    <line x1="0" y1="146" x2="1200" y2="146" stroke="var(--rule-blue)" stroke-width="6"/>
    <line x1="1040" y1="20" x2="1040" y2="590" stroke="var(--rule-blue)" stroke-width="6"/>
    <line x1="106" y1="24" x2="0" y2="290" stroke="var(--rule-blue)" stroke-width="6"/>
  </svg>

  <div class="header-band">
    <span class="header-letter">B</span>
    <span class="header-letter">R</span>
    <span class="header-letter">I</span>
    <span class="header-letter">G</span>
    <span class="header-letter">H</span>
    <span class="header-letter">T</span>
    <span class="header-letter">v</span>
    <span class="header-letter">a</span>
    <span class="header-letter">n</span>
    <span class="header-letter">e</span>
  </div>

  <h1 class="person-name">Owen Palfrey,</h1>

  <ul class="contact-list">
    <li>Cell&nbsp;&nbsp;&nbsp;: 027 918 603,</li>
    <li>Email: brightvane@mailnest.co.nz,</li>
    <li>www.brightvane.co.nz</li>
  </ul>

  <div class="partner-badge">dorvel</div>

  <div class="brand-lockup">
    <span class="brand-lockup-square"></span>
    <span class="brand-lockup-name">Brightvane</span>
  </div>

  <div class="corner-tile">dorvel</div>
</div>
</body>
</html>
```